Professional banners for an eyewear company

I have 3 images which need to be made into banners. Size 990 x 370, with a 10 pixel white border at top and bottom of banner.

They all need to be adjusted to make the colours better and less bright.
All will need some writing written on them with a nice serif font.

Banner 1 text: Handcrafted luxury eyewear, with a purpose...
Banner 2 text: Half of our profits go to help malnourished children in India
Banner 3 text: 10% of your first order, use code: First Order

On our homepage these 3 banners will alternate, so they need to look good together.

Tips
Please take a look at the banners on the lunvoreck.com homepage, this is kind of how I want the text to be displayed, and they use good colours.

The backgrounds on Banners 2 & 3 can be changed.
Banner 3 background if you can change to a nice colour, as per lunvoreck.com homepage.
Updates

Hi, just a quick update, thank you for all the designs submitted so far, please keep in mind that the brand is a luxury high-end brand so designs will need to reflect this.

Industry/Entity Type

Eyewear

```html
<!DOCTYPE html>
<html lang="en">
<head>
<meta charset="utf-8">
<title>First Order Offer Banners</title>
<link rel="stylesheet" href="https://fonts.googleapis.com/css2?family=Forum&family=Source+Sans+3:wght@400&display=swap">
<style>
  :root {
    --page: #ffffff;
    --ink-light: #ffffff;
    --note: #f6e48c;
    --note-ink: #2a2118;
    --note-shadow: #3b302b;
    --cocoa-deep: #33211c;
    --cocoa-mid: #6e5248;
    --cocoa-low: #9c7d70;
    --cocoa-glow: #ece6e3;
    --rose-deep: #df4f58;
    --rose-mid: #e7848a;
    --rose-low: #eedfd8;
    --rose-glow: #fbf0f0;
  }
  * { margin: 0; padding: 0; box-sizing: border-box; }
  html, body {
    width: 1200px;
    height: 951px;
    overflow: hidden;
    background: var(--page);
  }
  .banner {
    position: absolute;
    left: 24px;
    width: 1153px;
    height: 429px;
    overflow: hidden;
  }
  .banner--cocoa {
    top: 26px;
    background:
      radial-gradient(ellipse 360px 330px at 330px 215px, var(--cocoa-glow) 0%, rgba(236,230,227,0.55) 40%, rgba(236,230,227,0) 100%),
      linear-gradient(170deg, var(--cocoa-deep) 0%, var(--cocoa-mid) 55%, var(--cocoa-low) 100%);
  }
  .banner--rose {
    top: 496px;
    background:
      radial-gradient(ellipse 380px 340px at 330px 230px, var(--rose-glow) 0%, rgba(251,240,240,0.6) 40%, rgba(251,240,240,0) 100%),
      linear-gradient(175deg, var(--rose-deep) 0%, var(--rose-mid) 50%, var(--rose-low) 100%);
  }
  .model-photo {
    position: absolute;
    left: 80px;
    top: 8px;
    width: 440px;
    height: 421px;
    border-radius: 46% 46% 0 0 / 40% 40% 0 0;
    background:
      radial-gradient(ellipse 120px 170px at 52% 38%, rgba(196,106,58,0.85) 0%, rgba(178,88,44,0.6) 55%, rgba(178,88,44,0) 100%),
      linear-gradient(180deg, rgba(210,140,100,0.25) 0%, rgba(236,225,218,0.9) 70%, #ebe2dc 100%);
  }
  .sticky-note {
    position: absolute;
    left: 592px;
    top: 98px;
    width: 160px;
    height: 170px;
  }
  .offer {
    position: absolute;
    left: 746px;
    top: 160px;
    color: var(--ink-light);
  }
  .offer__headline {
    font-family: "Forum", serif;
    font-weight: 400;
    font-size: 45px;
    line-height: 52px;
    letter-spacing: 1.5px;
    text-transform: uppercase;
  }
  .offer__code {
    margin-top: 14px;
    font-family: "Source Sans 3", sans-serif;
    font-size: 25px;
    line-height: 30px;
  }
</style>
</head>
<body>

  <section class="banner banner--cocoa">
    <div class="model-photo" role="img" aria-label="Photo of a red-haired woman in sunglasses and a polka dot blouse, looking surprised"></div>
    <svg class="sticky-note" viewBox="0 0 160 170" aria-hidden="false">
      <polygon points="12,138 118,158 130,162 20,146" fill="var(--note-shadow)"/>
      <g transform="rotate(10 80 80)">
        <rect x="20" y="18" width="122" height="124" fill="var(--note)"/>
        <text x="80" y="94" text-anchor="middle" font-family="Forum, serif" font-size="46" fill="var(--note-ink)">10%</text>
      </g>
    </svg>
    <div class="offer">
      <h2 class="offer__headline">Of your<br>first order,</h2>
      <p class="offer__code">use code: First Order</p>
    </div>
  </section>

  <section class="banner banner--rose">
    <div class="model-photo" role="img" aria-label="Photo of a red-haired woman in sunglasses and a polka dot blouse, looking surprised"></div>
    <svg class="sticky-note" viewBox="0 0 160 170">
      <polygon points="12,138 118,158 130,162 20,146" fill="var(--note-shadow)"/>
      <g transform="rotate(10 80 80)">
        <rect x="20" y="18" width="122" height="124" fill="var(--note)"/>
        <text x="80" y="94" text-anchor="middle" font-family="Forum, serif" font-size="46" fill="var(--note-ink)">10%</text>
      </g>
    </svg>
    <div class="offer">
      <h2 class="offer__headline">Of your<br>first order,</h2>
      <p class="offer__code">use code: First Order</p>
    </div>
  </section>

</body>
</html>
```